Business and Success Coaching Business Card

Need a business card for my coaching business. I coach small businesses, career professionals and, individuals wanting to unlock their human potential and achieve excellence. At the heart of our methodology is the Shaping Purposeful Action Routines Knowingly (SPARK) approach to formulate empowerment, create principles for success and setting achievable outcomes. I would like something that incorporates our new logo, something clean and sharp with a solid darker, but complementary background, color on the card front. The back should be white where there will be room for three questions

Target Market(s)

People looking to advance and improve themselves through a success coach

Industry/Entity Type

Life Coaching

Contact Information for Business Card

Contact information on card.
Business name on front of card
Questions on back

Font styles to use
Other font styles liked:
• Century Gothic or other Serif style fonts that look similar to Century Gothic

Colors

Designer to choose colors to be used in the design.

Requirements
Must have
• Logo on front of card
• Business name - The Steady Forge
• Contact name - Ted Harlow
• Address - Box 4619, Littleton, CO 80127-4619
• Phone number - 303-555-0147
• Email address - harlow.ted@thesteadyforge.example
• Certifications - CSC, CCHt, PTT, PNLP
• Back of card
• Three questions on the back of the card:
• If you were at your best, what would you do right now?
• What is the decision you have been avoiding?
• What's one action you could take in the next 10 minutes?
Nice to have
• I would like to see a solid color on the front of the card that compliments the logo.
• Back should be white, or could be contrasting, but need to have the three questions.

```html
<!DOCTYPE html>
<html lang="en">
<head>
<meta charset="utf-8">
<title>The Steady Forge – Business Card</title>
<link rel="stylesheet" href="https://fonts.googleapis.com/css2?family=Jost:wght@400;500;600;700&display=swap">
<style>
  :root {
    --stage: #2b2b2d;
    --card-white: #ffffff;
    --navy-text: #1f3a7a;
    --band-blue: #4a86cc;
    --front-dark: #0e1428;
    --front-dark-2: #141c36;
    --accent-blue: #3f74c4;
    --light-text: #e6e9f0;
    --muted-text: #c9cfdc;
  }
  * { box-sizing: border-box; margin: 0; padding: 0; }
  html, body { width: 1200px; height: 880px; overflow: hidden; }
  body {
    background: var(--stage);
    font-family: "Jost", "Century Gothic", sans-serif;
    position: relative;
  }
  .card {
    position: absolute;
    left: 250px;
    width: 700px;
    height: 400px;
    border-radius: 22px;
    overflow: hidden;
  }

  /* Back side */
  .card-back { top: 20px; background: var(--card-white); }
  .questions {
    position: absolute;
    top: 0; left: 0; right: 0; bottom: 52px;
    display: flex; flex-direction: column;
    justify-content: center; align-items: center;
    gap: 10px;
    color: var(--navy-text);
    font-weight: 600;
    font-size: 27px;
    text-align: center;
    line-height: 1.15;
  }
  .web-band {
    position: absolute;
    left: 0; right: 0; bottom: 0;
    height: 52px;
    background: var(--band-blue);
    color: var(--card-white);
    display: flex; align-items: center; justify-content: center;
    font-size: 16px;
    letter-spacing: 0.62em;
    text-transform: uppercase;
  }

  /* Front side */
  .card-front {
    top: 460px;
    background: linear-gradient(135deg, var(--front-dark-2), var(--front-dark));
    color: var(--light-text);
  }
  .brand {
    position: absolute;
    left: 40px; top: 150px;
    width: 330px;
    text-align: center;
  }
  .brand-mark {
    width: 26px; height: 26px;
    border-radius: 50%;
    background: var(--accent-blue);
    margin: 0 auto 14px;
  }
  .brand-name {
    color: var(--accent-blue);
    font-weight: 600;
    font-size: 36px;
    line-height: 1;
  }
  .brand-tagline {
    margin-top: 6px;
    font-size: 20px;
    color: var(--light-text);
  }
  .divider {
    position: absolute;
    left: 392px; top: 92px;
    width: 1.5px; height: 216px;
    background: var(--muted-text);
  }
  .contact {
    position: absolute;
    left: 416px; top: 88px;
    right: 20px;
  }
  .person-name {
    font-weight: 700;
    font-size: 25px;
    text-transform: uppercase;
    letter-spacing: 0.02em;
  }
  .credentials {
    color: var(--accent-blue);
    font-size: 19px;
    margin-top: 2px;
  }
  .address {
    margin-top: 12px;
    font-size: 17px;
    line-height: 1.3;
    color: var(--muted-text);
  }
  .contact-list {
    list-style: none;
    margin-top: 14px;
    font-size: 15.5px;
    color: var(--muted-text);
  }
  .contact-list li {
    display: flex; align-items: center; gap: 10px;
    line-height: 1.55;
  }
  .contact-list svg { width: 14px; height: 14px; flex: none; fill: var(--accent-blue); }
</style>
</head>
<body>

<section class="card card-back" aria-label="Card back">
  <div class="questions">
    <p>If you were at your best, what would you do right now?</p>
    <p>What is the decision you have been avoiding?</p>
    <p>What's one action you could take in the next 10 minutes?</p>
  </div>
  <div class="web-band">www.thesteadyforge.example</div>
</section>

<section class="card card-front" aria-label="Card front">
  <div class="brand">
    <div class="brand-mark"></div>
    <div class="brand-name">The Steady Forge</div>
    <div class="brand-tagline">Jump-start your next phase</div>
  </div>
  <div class="divider"></div>
  <div class="contact">
    <div class="person-name">Ted Harlow</div>
    <div class="credentials">CSC, CCHt, PTT, PNLP</div>
    <div class="address">Box 4619, Littleton<br>CO 80127-4619</div>
    <ul class="contact-list">
      <li>
        <svg viewBox="0 0 24 24" aria-hidden="true"><path d="M6.6 10.8a15.1 15.1 0 0 0 6.6 6.6l2.2-2.2a1 1 0 0 1 1-.25 11.4 11.4 0 0 0 3.6.57 1 1 0 0 1 1 1V20a1 1 0 0 1-1 1A17 17 0 0 1 3 4a1 1 0 0 1 1-1h3.5a1 1 0 0 1 1 1c0 1.25.2 2.45.57 3.57a1 1 0 0 1-.25 1z"/></svg>
        303-555-0147
      </li>
      <li>
        <svg viewBox="0 0 24 24" aria-hidden="true"><path d="M2 5h20v14H2z M2 5l10 8 10-8" fill="none" stroke="#3f74c4" stroke-width="2.4"/></svg>
        harlow.ted@thesteadyforge.example
      </li>
      <li>
        <svg viewBox="0 0 24 24" aria-hidden="true"><g fill="none" stroke="#3f74c4" stroke-width="2"><circle cx="12" cy="12" r="10"/><ellipse cx="12" cy="12" rx="4.5" ry="10"/><path d="M2 12h20M4 7h16M4 17h16"/></g></svg>
        www.thesteadyforge.example
      </li>
    </ul>
  </div>
</section>

</body>
</html>
```